Typography Tattoo

I'm looking to tattoo a particular phrase onto my arm and I'm hoping to find the right artist who can create an interesting piece using the phrase "THIS TOO SHALL PASS" using either part or all of the phrase in English, Russian and Hebrew:
English: "THIS TOO SHALL PASS"
Russian: "ЭТО ТОЖЕ ПРОЙДЕТ"
Hebrew: "גם זה יעבור"
Three Notes:
1. In a perfect world the order would be Hebrew, Russian and English. With most of the focus being on the English.
2. Hebrew is read from right to left.
3. I wouldn't mind if you found a way to turn the Hebrew or Russian into shapes that put the focus back on the English.
I'm including a few images:
1. One illustrates the direction of the tattoo as I invision it. I imagine a long continuous piece that wraps around the arm.
2. Another image shows the text in a very crudely photoshopped way.
3.The third shows another version of the Hebrew which just shows the first symbol in each word, its a sort of shorthand (if you can find a creative way to use this I'd be happy, but I'm open to anything.)
Again, you don't have to use all these languages, I'm mostly looking for something cool looking - your art will be on my body for the rest of my life so I want it to - above all else - look good.
Though the Font and look of the text is important, I'm very open to artistic renderings, I don't need something that is just words.
Edit 2/27: Thanks everyone so far, I've just uploaded a series of images that show the design I'm hoping someone can create cleanly - gotta find a font or hand-draw so the text looks the same across all three languages, and the plan is to have it wrap around my arm at least once, so length is key. One other thought is that I'm really open to including a design around the font or someway of making the break between the three languages stand out more. Thanks!
Reason: A bunch of new designs came in and I want to give everyone time to respond to my notes.

```html
<!DOCTYPE html>
<html lang="en">
<head>
<meta charset="utf-8">
<title>This Too Shall Pass — Typography Tattoo</title>
<link rel="stylesheet" href="https://fonts.googleapis.com/css2?family=Rubik:wght@500;600&display=swap">
<style>
  :root {
    --paper: #ffffff;
    --ink: #000000;
  }
  html, body {
    margin: 0;
    padding: 0;
    width: 1200px;
    height: 900px;
    overflow: hidden;
    background: var(--paper);
  }
  .tattoo {
    display: block;
    width: 1200px;
    height: 900px;
  }
  .phrase {
    font-family: "Rubik", sans-serif;
    fill: var(--ink);
  }
  .phrase--hebrew {
    font-size: 54px;
    font-weight: 500;
    direction: ltr;
    unicode-bidi: bidi-override;
  }
  .phrase--english {
    font-size: 66px;
    font-weight: 600;
  }
  .phrase--russian {
    font-size: 60px;
    font-weight: 500;
  }
</style>
</head>
<body>
<svg class="tattoo" viewBox="0 0 1200 900" xmlns="http://www.w3.org/2000/svg">
  <text class="phrase phrase--hebrew" x="628" y="357" textLength="494" lengthAdjust="spacing">גם זה יעבור</text>
  <text class="phrase phrase--english" x="78" y="458" textLength="1044" lengthAdjust="spacing">THIS TOO SHALL PASS</text>
  <text class="phrase phrase--russian" x="82" y="565" textLength="723" lengthAdjust="spacing">ЭТО ТОЖЕ ПРОЙДЕТ</text>
</svg>
</body>
</html>
```